2nd Opinion Radiology web page

Looking for a web page design for second opinion radiology service. Main page will have a link directing user to locate CD on their computer/device, and will take contents of CD and upload to server, which I will specify.

Web page needs a form to enter user's name, contact info, and create a log in for user. User must click to accept terms of service, which will be a paragraph which i will provide. User will log back in, after uploading cd, to find report, which will be able to be viewed once user pays, by zumbit. User will need to be able to download report.

There will be a small paragraph explaining what we do: Provide expert second opinions, worldwide. We provide interpretations from radiologists with many years of experience and training from the world's best institutions, including corwent and halvering general hospital.

A second paragraph: Have questions or doubts about your CT or MRI? Get a second opinion from experts at Vexorly. Tap into the full potential of your images.

Thanks
Updates

Reason: The website does not need to be fully coded, however, should include graphics and design so a web designer can simply take the design, images, and objects and code the site.

Target Market(s)

People who are unsure of their medical care and looking for a second opinion.

Industry/Entity Type

Training

Files

```html
<!DOCTYPE html>
<html lang="en">
<head>
<meta charset="utf-8">
<title>Second Opinion Radiology – Locate CD</title>
<link rel="stylesheet" href="https://fonts.googleapis.com/css2?family=Roboto:wght@300;400&family=Nunito:wght@900&display=swap">
<style>
:root{
  --sky:#9bd3f5;
  --sky-pale:#b9e0f6;
  --band-grey:#c5cacf;
  --footer:#93c5e3;
  --accent:#02aefc;
  --link:#7cc9f2;
  --text-grey:#8f8f8f;
  --field-border:#d0d0d0;
  --dark-text:#444;
  --white:#fff;
}
*{margin:0;padding:0;box-sizing:border-box}
html,body{width:1200px;height:1196px;overflow:hidden}
body{position:relative;background:var(--white);font-family:"Roboto",Arial,sans-serif;font-weight:300}
.abs{position:absolute}

.header{left:0;top:0;width:1200px;height:140px;background:linear-gradient(#fff,#f3f3f3)}
.brand{left:42px;top:36px;display:flex;align-items:center;gap:20px}
.brand-dot{width:66px;height:66px;border-radius:50%;border:2px solid #b8c3d8}
.brand-name{font-size:29px;color:#7a8fcf;font-weight:300}
.nav a{position:absolute;top:55px;font-size:22px;color:var(--link);text-decoration:none}
.nav .active{left:593px;top:50px;width:99px;height:36px;line-height:36px;text-align:center;border-radius:6px;background:#f6f6f6;box-shadow:0 1px 4px rgba(0,0,0,.15)}

.top-band{left:0;top:140px;width:1200px;height:21px;background:var(--sky)}
.hero{left:0;top:161px;width:1200px;height:382px;background:linear-gradient(#fff,#f7f7f7)}
.portrait{left:205px;top:168px;width:190px;height:185px;background:linear-gradient(#e7e7e7,#f4f4f4);border-radius:40% 40% 0 0}
.hero-q{left:521px;top:248px;font-size:28px;color:var(--text-grey)}
.hero-h{left:521px;top:284px;font-size:47px;color:var(--text-grey)}

.form-band{left:0;top:543px;width:1200px;height:372px;background:var(--sky)}
.form-band-top{left:0;top:543px;width:1200px;height:20px;background:var(--sky-pale)}
.grey-band{left:0;top:915px;width:1200px;height:63px;background:var(--band-grey)}
.welcome{left:90px;top:586px;width:432px;height:392px;background:var(--white);border-radius:6px 6px 0 0;padding:22px 20px}
.welcome h2{font-weight:300;font-size:30px;color:var(--text-grey);margin-bottom:12px}
.welcome p{font-size:15.5px;line-height:26.5px;color:var(--text-grey);text-align:justify;margin-bottom:18px}
.right-panel{left:522px;top:563px;width:678px;height:415px;background:var(--sky)}
.right-panel-foot{left:522px;top:915px;width:678px;height:63px;background:var(--band-grey)}
.bg-field{background:var(--white);border-radius:5px;height:51px;padding:12px 16px;font-size:22px;color:var(--link)}
.bg-check{left:565px;top:853px;width:31px;height:31px;background:var(--white)}
.bg-terms{left:609px;top:856px;font-size:22px;color:var(--white)}
.bg-terms span{color:#5d7a8e}
.bg-submit{left:782px;top:920px;width:125px;height:51px;background:var(--white);border-radius:4px;text-align:center;line-height:51px;font-size:22px;color:var(--link)}

.veil{left:0;top:0;width:1200px;height:1196px;background:rgba(255,255,255,.35)}

.footer{left:0;top:1116px;width:1200px;height:80px;background:var(--footer)}
.footer-links{right:25px;top:11px;font-size:17.5px;color:var(--white);font-weight:400}

.modal{left:169px;top:345px;width:841px;height:382px;background:var(--white);box-shadow:0 0 6px rgba(0,0,0,.12)}
.modal-bar{height:57px;background:var(--accent);display:flex;justify-content:space-between;align-items:center;padding:0 22px}
.modal-title,.modal-close{font-family:"Nunito",Arial,sans-serif;font-weight:900;font-size:29px;color:var(--white);letter-spacing:.5px}
.field{position:absolute;border:2px solid var(--field-border);border-radius:4px;height:61px;padding:0 22px;line-height:57px;font-size:22px;color:var(--dark-text);font-weight:400}
.btn{position:absolute;background:var(--accent);color:var(--white);border-radius:6px;text-align:center;font-weight:300}
.check{position:absolute;left:47px;top:277px;width:47px;height:47px;border:2px solid #9a9a9a;border-radius:7px}
.check-label{position:absolute;left:110px;top:281px;font-size:27px;color:var(--dark-text);font-weight:400}
</style>
</head>
<body>
  <header class="abs header">
    <div class="abs brand"><div class="brand-dot"></div><span class="brand-name">companyname</span></div>
    <nav class="nav">
      <a class="active" href="#">home</a>
      <a href="#" style="left:737px">company</a>
      <a href="#" style="left:892px">services</a>
      <a href="#" style="left:1022px">contact us</a>
    </nav>
  </header>
  <div class="abs top-band"></div>
  <section class="abs hero"></section>
  <div class="abs portrait" role="img" aria-label="Photo of a smiling radiologist in a white coat with a stethoscope"></div>
  <p class="abs hero-q">Have questions or doubts about your CT or MRI?</p>
  <p class="abs hero-h">Get a second opinion from</p>

  <div class="abs form-band"></div>
  <div class="abs form-band-top"></div>
  <div class="abs grey-band"></div>
  <div class="abs right-panel"></div>
  <div class="abs right-panel-foot"></div>
  <article class="abs welcome">
    <h2>Welcome</h2>
    <p>Lorem ipsum dolor sit amet, consectetur adipisicing elit, sed do eiusmod tempor incididunt ut labore et dolore magna aliqua. Ut enim ad minim veniam.</p>
    <p>Lorem ipsum dolor sit amet, consectetur adipisicing elit, sed do eiusmod tempor incididunt ut labore et dolore magna aliqua. Ut enim ad minim veniam.</p>
  </article>
  <div class="abs bg-field" style="left:878px;top:630px;width:292px"></div>
  <div class="abs bg-field" style="left:558px;top:702px;width:293px">Email</div>
  <div class="abs bg-field" style="left:878px;top:702px;width:292px">Username</div>
  <div class="abs bg-field" style="left:560px;top:783px;width:293px">Mobile No.</div>
  <div class="abs bg-field" style="left:878px;top:781px;width:292px">Password</div>
  <div class="abs bg-check"></div>
  <p class="abs bg-terms">Check if you agree to the <span>Terms and Agreements</span></p>
  <div class="abs bg-submit">Submit</div>

  <footer class="abs footer"><p class="abs footer-links">Privacy Policy | Terms | Copyright | Contact Us</p></footer>

  <div class="abs veil"></div>

  <section class="abs modal" aria-label="Locate CD">
    <div class="modal-bar"><span class="modal-title">LOCATE CD</span><span class="modal-close">X</span></div>
    <div class="field" style="left:41px;top:89px;width:519px">Specify Path...</div>
    <div class="btn" style="left:579px;top:88px;width:135px;height:61px;line-height:61px;font-size:38px">PATH</div>
    <div class="field" style="left:41px;top:196px;width:372px">Username</div>
    <div class="field" style="left:437px;top:196px;width:371px">Password</div>
    <div class="check"></div>
    <span class="check-label">Check to Agree to the Terms</span>
    <div class="btn" style="left:585px;top:277px;width:174px;height:69px;line-height:69px;font-size:32px;border-radius:4px">Submit</div>
  </section>
</body>
</html>
```